" O escritório de advocacia atua de forma estratégica e personalizada, oferecendo assessoria jurídica completa com foco na excelência técnica, na ética profissional e na construção de soluções eficazes para seus clientes. O atendimento é conduzido diretamente pelos sócios, garantindo proximidade, confiança e alto nível de especialização em cada demanda. Cada caso é analisado de maneira individualizada, com abordagem analítica, planejamento jurídico preciso e comunicação clara. O escritório combina tradição jurídica e visão contemporânea, utilizando métodos atualizados, organização eficiente e atuação responsável para entregar segurança jurídica e resultados consistentes. "

```html
<!DOCTYPE html>
<html lang="pt-BR">
<head>
<meta charset="utf-8">
<title>Pasta – Moraes &amp; Salles Advogados</title>
<link href="https://fonts.googleapis.com/css2?family=Montserrat:wght@600&display=swap" rel="stylesheet">
<style>
  :root {
    --navy: #0f2a4a;
    --navy-edge: #0a1f38;
    --paper: #ffffff;
    --silver: #8f8f8f;
    --backdrop: #e9e6e2;
  }
  html, body {
    margin: 0;
    width: 1200px;
    height: 1200px;
    overflow: hidden;
    background: var(--backdrop);
  }
  .folder {
    position: relative;
    width: 1200px;
    height: 1200px;
  }
  .folder-shape {
    position: absolute;
    inset: 0;
  }
  .brand {
    position: absolute;
    display: flex;
    align-items: center;
    font-family: "Montserrat", sans-serif;
    font-weight: 600;
    letter-spacing: 0.08em;
    line-height: 1.2;
    white-space: nowrap;
  }
  .brand-square {
    flex: none;
    background: currentColor;
  }

  .brand--cover {
    left: 700px;
    top: 516px;
    color: var(--silver);
    font-size: 30px;
    gap: 18px;
  }
  .brand--cover .brand-square { width: 22px; height: 22px; }

  .brand--back {
    left: 290px;
    top: 776px;
    color: var(--paper);
    font-size: 14px;
    gap: 9px;
  }
  .brand--back .brand-square { width: 10px; height: 10px; }

  .address {
    position: absolute;
    left: 132px;
    width: 468px;
    top: 826px;
    margin: 0;
    text-align: center;
    font-family: "Montserrat", sans-serif;
    font-weight: 600;
    font-size: 11px;
    color: var(--paper);
  }
</style>
</head>
<body>
<main class="folder">
  <svg class="folder-shape" width="1200" height="1200" viewBox="0 0 1200 1200" aria-hidden="true">
    <rect x="132" y="216" width="468" height="876" fill="var(--navy)"/>
    <polygon points="36,990 132,990 132,1092 600,1092 600,1128 60,1128 36,1104" fill="var(--navy)"/>
    <polyline points="132,990 132,1092 600,1092" fill="none" stroke="var(--navy-edge)" stroke-width="2"/>
    <rect x="600" y="216" width="480" height="636" fill="var(--paper)"/>
    <rect x="600" y="830" width="480" height="22" fill="var(--navy)"/>
  </svg>

  <div class="brand brand--cover">
    <span class="brand-square"></span>
    <span class="brand-name">MORAES &amp; SALLES<br>ADVOGADOS</span>
  </div>

  <div class="brand brand--back">
    <span class="brand-square"></span>
    <span class="brand-name">MORAES &amp; SALLES<br>ADVOGADOS</span>
  </div>

  <p class="address">Rua Lisboa, 24 - Sala 804 - Centro - Rio de Janeiro | RJ</p>
</main>
</body>
</html>
```